New letter head for Air Conditioning business

We need a new professional letter head design to suit our new re-branded air conditioning business. Our new logo is attached

```html
<!DOCTYPE html>
<html lang="en">
<head>
<meta charset="utf-8">
<title>Nordvane Letterhead</title>
<link rel="stylesheet" href="https://fonts.googleapis.com/css2?family=Didact+Gothic&display=swap">
<style>
:root{
  --backdrop:#dcdcdc;
  --paper:#ffffff;
  --ink:#3a3a3a;
  --ink-soft:#444444;
  --brand-dark:#2f2f33;
  --brand-green:#5bbf7f;
  --brand-red:#ef6a5c;
  --band-green:#66c089;
}
*{box-sizing:border-box;margin:0;padding:0}
html,body{width:1083px;height:1200px;overflow:hidden;background:var(--backdrop)}
body{font-family:"Didact Gothic",sans-serif;color:var(--ink)}
.letterhead{position:absolute;left:130px;top:20px;width:822px;height:1160px;background:var(--paper);box-shadow:0 4px 18px rgba(0,0,0,.18);overflow:hidden}
.brand{position:absolute;left:48px;top:58px;display:flex;align-items:center;gap:14px}
.brand-dot{width:20px;height:20px;border-radius:50%;background:var(--brand-green)}
.brand-text{display:flex;flex-direction:column}
.brand-name{font-size:38px;letter-spacing:5px;color:var(--brand-dark);line-height:1}
.brand-tagline{font-size:9.5px;letter-spacing:2px;color:var(--brand-green);margin-top:6px;font-weight:bold}
.contact{position:absolute;right:47px;top:65px;list-style:none;text-align:right;font-size:14px;line-height:17px;color:var(--ink-soft)}
.contact li{display:flex;justify-content:flex-end;align-items:center;gap:6px}
.contact svg{width:10px;height:10px;fill:var(--brand-green)}
.recipient{position:absolute;left:48px;top:276px;font-size:15px;line-height:23.5px;font-style:normal}
.body{position:absolute;left:48px;top:408px;width:727px;font-size:15px;line-height:23.5px;text-align:justify;letter-spacing:.35px}
.body p{margin-bottom:22px}
.body p.closing{margin-bottom:12px;text-align:left}
.signature{width:150px;height:62px;border-radius:4px;background:linear-gradient(90deg,#f1f1f1,#e6e6e6)}
.footer{position:absolute;left:0;bottom:0;width:822px;height:46px}
.footer-rule{position:absolute;left:0;top:0;width:100%;height:5px;background:var(--brand-red)}
.footer-band{position:absolute;left:0;top:9px;width:100%;height:37px;background:var(--band-green)}
.address{position:absolute;left:63px;bottom:11px;color:#fff;font-size:15px}
</style>
</head>
<body>
<main class="letterhead">
  <header>
    <div class="brand">
      <span class="brand-dot"></span>
      <div class="brand-text">
        <span class="brand-name">NORDVANE</span>
        <span class="brand-tagline">AIR CONDITIONING &amp; REFRIGERATION</span>
      </div>
    </div>
    <ul class="contact">
      <li>555-014-2207 <svg viewBox="0 0 10 10"><path d="M2 0l2 2-1 1.5c.8 1.6 2 2.8 3.5 3.5L8 6l2 2-1.5 2C4 9.5.5 6 0 1.5z"/></svg></li>
      <li>555-018-3364 <svg viewBox="0 0 10 10"><rect x="2.5" y="0" width="5" height="3"/><rect x="0" y="3.5" width="10" height="4"/><rect x="2.5" y="6.5" width="5" height="3.5"/></svg></li>
      <li>hello@nordvaneair.com <svg viewBox="0 0 10 10"><path d="M0 2h10v6H0z M0 2l5 3.5L10 2" stroke="#fff" stroke-width=".6"/></svg></li>
      <li>www.nordvaneair.com <svg viewBox="0 0 10 10"><circle cx="5" cy="5" r="5"/></svg></li>
    </ul>
  </header>

  <address class="recipient">
    Mr/s<br>First Name and Last Name<br>Company Name<br>Address
  </address>

  <section class="body">
    <p>Placeholder copy is simple sample text used by the printing and typesetting trade. It has served as the usual stand-in text for a very long time, ever since early printers set loose lines of type to build a specimen sheet for their clients. It has lasted through many changes in the craft, including the move into digital layout, while staying much the same. It became even more common once printed sheets of sample paragraphs were sold widely to designers.</p>
    <p>The standard passage of sample copy has been used for generations and is shown here for anyone who is interested. Sections from an old essay on duty and pleasure by an early scholar are also shown in their exact first form, joined by an English version from a later translation. Sample text keeps a steady rhythm, a calm tone and a familiar shape, so it fills a page well while the real wording is still being written.</p>
    <p>It is a well known fact that a reader will be drawn away by the readable content of a page when looking at its layout. The point of using sample copy is that it has a fairly normal spread of letters, as opposed to using 'text goes here, text goes here', so it looks much like readable English. Many layout programs and web page editors now use it by default.</p>
    <p class="closing">Your Sincerely,</p>
    <div class="signature" role="img" aria-label="Handwritten signature"></div>
  </section>

  <footer class="footer">
    <div class="footer-rule"></div>
    <div class="footer-band"></div>
    <span class="address">1840 W. Harbor Lane, Suite 210 Oakridge, CA 90417</span>
  </footer>
</main>
</body>
</html>
```